Packaging design layout for specified cardboard box for 6 wine bottles

Need a design for a already specified cardboard box (called pakrafold) for my wine bottles. There fit 6 bottles a 750ml in it. Please only 3 colors. Attention Flexo Printing

Please find attached
- the font from the label Conte Varesi
- the label with the crest
- the PAKRAFOLD 6 BOTT, size of the box
-sample pictures of other brands for the same box, see IMG
and others...

The fonts have to be big, so that you are able to read them easily also from a distance. Like visible in picture (see attached) 9298 there is also the possibility to print inside the box. Its very important that you can see the brand name Conte Varesi and the crest very good.

Please choose also the color of the box. The wine label is something around Pantone's® color #705 Floral White. I also like a lot boxes in the natural color, havanna (so no color on). I uploaded a picture from our wineyard, maybe you can but it like a backrgound on the box (maybe as a painting or in white and black)

Requirements
Must have
• The following has to be written on the box:
• Product of Italy
• Tenuta Conte Varesi
• Via Monte Sorbo 14
• 39044 Egna
• Italia
• Tenuta Conte Varesi
• Birkenhofweg 14
• 39044 Neumarkt
• Italien
• - +39 0471563829
• - www.contevaresi.example
• - Facebook Conte Varesi
• - bar code
• - Logo "Stillen Rebgärtner" (see attached) - on one side of the box, you can make it also in another color, Logo of ARCU
• - "Contains 6 wine bottles x 750ml"
• - Net content litres 4,5
• - HEAVY
• - FRAGILE - on one side of the box
• - space for the wine label 10cm x 10xm (please not on top of the box, make a small border)
• - Font of CONTE VARESI
• - The crest of the Logo, please use the one of the designer qzpt or the one in Conte Varesi Gray Anchor (booth attached).
Nice to have
• I attached a painting, that is used on my wine bottle. Maybe you can somehow include it. Or I can use it like a seal to guarantee that the box was not open before. I prefer minimalism design. The fonts have to be big, so that you are able to read them easily also from a distance. Like visible in picture (see attached) 9298 there is also the possibility to print inside the box.

```html
<!DOCTYPE html>
<html lang="en">
<head>
<meta charset="utf-8">
<title>Conte Varesi – Wine Box Panel</title>
<link rel="stylesheet" href="https://fonts.googleapis.com/css2?family=Josefin+Sans:wght@600&family=Open+Sans:ital,wght@1,400&display=swap">
<style>
  :root {
    --wine-red: #a82036;
    --panel-grey: #e9eaea;
    --paper: #ffffff;
    --crest-grey: #d4d5d5;
    --dieline: #dddddd;
  }
  html, body {
    margin: 0;
    padding: 0;
    overflow: hidden;
    background: var(--paper);
  }
  .box-sheet {
    position: relative;
    width: 1200px;
    height: 902px;
    overflow: hidden;
    background: var(--paper);
    box-shadow: inset 0 0 0 1px var(--dieline);
  }
  .dieline-shapes {
    position: absolute;
    inset: 0;
  }
  .top-flap {
    position: absolute;
    left: 89px;
    top: 3px;
    width: 1051px;
    height: 162px;
    background: var(--wine-red);
  }
  .origin-line {
    position: absolute;
    left: 0;
    right: 0;
    top: 92px;
    margin: 0;
    text-align: center;
    font-family: "Open Sans", sans-serif;
    font-style: italic;
    font-size: 16px;
    letter-spacing: 0.3em;
    color: var(--paper);
  }
  .front-panel {
    position: absolute;
    left: 81px;
    top: 167px;
    width: 1066px;
    height: 610px;
    background: var(--panel-grey);
  }
  .crest-mark {
    position: absolute;
    left: 501px;
    top: 56px;
    width: 72px;
    height: 112px;
    background: var(--crest-grey);
  }
  .brand-name {
    position: absolute;
    left: 0;
    right: 0;
    top: 196px;
    margin: 0;
    text-align: center;
    font-family: "Josefin Sans", sans-serif;
    font-weight: 600;
    font-size: 54px;
    letter-spacing: 0.55em;
    padding-left: 0.55em;
    color: var(--wine-red);
  }
  .vineyard-scene {
    position: absolute;
    left: 0;
    right: 0;
    bottom: 0;
    height: 300px;
    background: linear-gradient(to bottom, var(--panel-grey) 0%, rgba(168, 32, 54, 0.55) 45%, var(--wine-red) 100%);
  }
</style>
</head>
<body>
  <div class="box-sheet">
    <svg class="dieline-shapes" width="1200" height="902" viewBox="0 0 1200 902" aria-hidden="true">
      <rect class="side-flap-top" x="1155" y="3" width="45" height="175" fill="var(--wine-red)"/>
      <polygon class="side-flap" points="1148,178 1200,178 1200,862 1150,778" fill="var(--wine-red)"/>
      <polygon class="bottom-flap" points="90,777 1150,777 1060,858 1100,902 120,902" fill="var(--wine-red)"/>
    </svg>

    <div class="top-flap">
      <p class="origin-line">Product of Italy</p>
    </div>

    <section class="front-panel">
      <div class="crest-mark" role="img" aria-label="Family crest of Conte Varesi"></div>
      <h1 class="brand-name">CONTE VARESI</h1>
      <div class="vineyard-scene" role="img" aria-label="Red line-art illustration of the estate vineyard with a rocky hillside and the manor house"></div>
    </section>
  </div>
</body>
</html>
```